2 sided postcard for New Internet Customers

We would like a design for a two sided postcard (with room for mailing label), dimensions 9 1/4 by 6 1/4 to be sent via US Mail.

The postcard needs to include our logo (attached) and the text
Fiber Optic Internet
555-219-8063
http://www.brightwirenet.example
Speeds up to 1 Gig, with packages starting at $55

These will be sent to people who do not have our service.

Since this is going to be "junk mail" we probably only have 1 second or less to capture someone's attention to encourage them to read the entire postcard.

We are a "mom and pop" telecommunications company that provides internet, phone, and television services on the fiber optic network that we designed, built, and maintain.

We started as a dial up ISP in 1995, and have extraordinary technical support based in Freeport PA, our customers actually get the speeds they pay for, and our service is highly reliable.

We have a slogan (which you can choose to use or ignore) which is
"I Went Fast with Kornwell"

Existing customers can earn a $50 credit for every new customer they refer to us. Unlike most large cable and internet companies we have very happy customers... some who have stayed with us for decades.

I've attached our previous postcard, which I really dislike. It does have a blank spot for where the mailing label should go.

Target Market(s)

New Internet Customers in Western Pennsylvania

Industry/Entity Type

Internet

Font styles to use
Other font styles liked:
• Just match our logo.

Colors

Designer to choose colors to be used in the design.

Requirements
Must have
• The postcard needs to include our logo, and the text Fiber Optic Internet 555-219-8063 http://www.brightwirenet.example Speeds up to 1 Gig, with packages starting at $55
Nice to have
• The colors and fonts should look good with our logo.
Should not have
• Should not have small print or lots of text. Both sides need to capture attention.

```html
<!DOCTYPE html>
<html lang="en">
<head>
<meta charset="utf-8">
<title>Kornwell Fiber Postcard</title>
<link rel="stylesheet" href="https://fonts.googleapis.com/css2?family=Roboto+Condensed:wght@300;400;700;900&family=Montserrat:wght@700;800&family=Lato:wght@400&display=swap">
<style>
:root{
  --brand-blue:#0a72bf;
  --deep-blue:#0a4f9a;
  --ink:#222326;
  --white:#ffffff;
  --backdrop:#e4e4e2;
  --stamp:#ececec;
}
*{margin:0;padding:0;box-sizing:border-box}
html,body{width:1200px;height:911px;overflow:hidden;background:var(--backdrop)}
.canvas{position:relative;width:1200px;height:911px}
.postcard{position:absolute;width:622px;height:420px;background:var(--white);overflow:hidden;box-shadow:0 6px 18px rgba(0,0,0,.18)}
.postcard--back{left:40px;top:24px}
.postcard--front{left:538px;top:467px}
.postcard svg.shape{position:absolute;left:0;top:0}
.brand{position:absolute;display:flex;align-items:center;gap:8px;font-family:"Lato",sans-serif;color:var(--ink)}
.brand__dot{border-radius:50%;background:var(--brand-blue)}
.postcard--back .brand{left:330px;top:14px;font-size:15px}
.postcard--back .brand__dot{width:36px;height:36px}
.postcard--front .brand{left:16px;top:13px;font-size:24px;gap:12px}
.postcard--front .brand__dot{width:56px;height:56px}
.stamp-box{position:absolute;left:576px;top:14px;width:33px;height:38px;background:var(--stamp);border-radius:3px}
.txt{position:absolute;font-family:"Roboto Condensed",sans-serif;color:var(--white);line-height:1}
.pride{left:14px;top:12px;font-weight:300;font-size:22px;line-height:25px;letter-spacing:-.3px}
.pitch{left:13px;top:98px;font-family:"Montserrat",sans-serif;font-weight:800;font-size:19px;line-height:25px;color:var(--white)}
.pitch span{color:var(--ink);display:block}
.referral{left:14px;top:191px;font-weight:300;font-size:24px;line-height:29px;letter-spacing:-.4px}
.referral b{font-weight:700}
.quote-mark{position:absolute;left:14px;top:162px}
.price{position:absolute;border-radius:50%;background:var(--brand-blue);border:4px solid var(--white);box-shadow:0 0 0 2px var(--brand-blue),0 3px 8px rgba(0,0,0,.25);text-align:center;color:var(--white)}
.price__label{font-family:"Montserrat",sans-serif;font-weight:700;font-size:12px;line-height:13px;margin-top:24px}
.price__amount{font-family:"Roboto Condensed",sans-serif;font-weight:900;font-size:52px;line-height:52px;letter-spacing:-1px}
.postcard--back .price{left:216px;top:118px;width:120px;height:120px}
.postcard--front .price{left:214px;top:216px;width:120px;height:120px}
.visit{font-family:"Montserrat",sans-serif;font-weight:400;font-size:12px}
.url{font-family:"Montserrat",sans-serif;font-size:15px;letter-spacing:2px;font-weight:400}
.url b{font-weight:800}
.call{position:absolute;height:27px;border-radius:14px;background:var(--ink);color:var(--white);font-family:"Roboto Condensed",sans-serif;font-weight:700;font-size:24px;line-height:27px;padding-left:16px;letter-spacing:-.6px}
.postcard--back .visit{left:14px;top:331px}
.postcard--back .url{left:14px;top:349px}
.postcard--back .call{left:13px;top:375px;width:296px}
.headline{position:absolute;left:13px;top:78px;font-family:"Roboto Condensed",sans-serif;font-weight:900;font-size:38px;color:var(--ink);letter-spacing:-1px}
.slogan{position:absolute;left:13px;top:128px;font-family:"Montserrat",sans-serif;font-weight:800;font-size:36px;line-height:38px;color:var(--brand-blue);letter-spacing:-.5px}
.slogan span{display:block;color:var(--ink);font-family:"Roboto Condensed",sans-serif;font-weight:900;font-size:46px;line-height:44px;letter-spacing:2px}
.speed{position:absolute;left:0;top:231px;width:208px;height:24px;border-radius:0 12px 12px 0;background:var(--brand-blue);color:var(--white);font-family:"Montserrat",sans-serif;font-weight:700;font-size:15px;line-height:24px;padding-left:16px}
.illustration{position:absolute;left:335px;top:38px;width:287px;height:330px;border-radius:40% 0 40% 50%;background:radial-gradient(circle at 45% 55%,#2e4f9e 0%,#14306f 45%,rgba(10,114,191,.35) 75%,rgba(255,255,255,0) 100%)}
.postcard--front .visit{left:34px;top:332px}
.postcard--front .url{left:34px;top:350px}
.postcard--front .call{left:15px;top:373px;width:320px;height:29px;line-height:29px;font-size:26px}
</style>
</head>
<body>
<main class="canvas">

  <section class="postcard postcard--back" aria-label="Postcard back">
    <svg class="shape" width="622" height="420" viewBox="0 0 622 420">
      <path d="M0 0 H310 C250 40 225 110 262 200 C300 280 360 330 297 420 H0 Z" fill="var(--brand-blue)"/>
      <path d="M316 0 C256 40 232 110 270 200 C308 282 368 332 304 420" fill="none" stroke="var(--ink)" stroke-width="7"/>
    </svg>
    <div class="brand"><span class="brand__dot"></span>Kornwell, Inc.</div>
    <div class="stamp-box"></div>
    <p class="txt pride">We are so proud of our service,<br>we haven’t changed our<br>name in over 28 years”</p>
    <p class="txt pitch">LOCAL, FAST, AND<span>RELIABLE INTERNET</span></p>
    <svg class="quote-mark" width="250" height="150" viewBox="0 0 250 150">
      <text x="0" y="30" font-family="Georgia,serif" font-size="46" font-weight="700" fill="var(--white)">“</text>
      <line x1="38" y1="14" x2="220" y2="14" stroke="var(--ink)" stroke-width="1.5"/>
      <path d="M220 14 H232 V135 H140" fill="none" stroke="var(--ink)" stroke-width="1.5"/>
    </svg>
    <p class="txt referral"><b>Existing customers</b><br>can earn a <b>$50</b> credit<br>for every <b>new customer</b><br>they <b>refer</b> to us</p>
    <div class="price"><div class="price__label">PACKAGES<br>STARTING @</div><div class="price__amount">$55</div></div>
    <p class="txt visit">VISIT US ONLINE @</p>
    <p class="txt url">www.<b>brightwirenet</b>.example</p>
    <div class="call">CALL US AT 555-219-8063</div>
  </section>

  <section class="postcard postcard--front" aria-label="Postcard front">
    <svg class="shape" width="622" height="420" viewBox="0 0 622 420">
      <circle cx="462" cy="284" r="152" fill="var(--brand-blue)"/>
      <path d="M0 420 V300 C40 265 80 300 130 320 C200 345 280 300 360 300 C470 300 530 380 622 380 V420 Z" fill="var(--brand-blue)"/>
      <path d="M0 330 C30 280 70 270 120 300 C140 312 150 318 170 322 C120 290 70 255 30 275 C12 285 4 300 0 310 Z" fill="var(--ink)"/>
      <path d="M400 330 C480 370 540 360 622 340 V372 C540 395 470 392 400 330 Z" fill="var(--ink)"/>
    </svg>
    <div class="illustration" role="img" aria-label="Coiled blue fiber optic cable with glowing connector and binary data streams"></div>
    <div class="brand"><span class="brand__dot"></span>Kornwell, Inc.</div>
    <h1 class="headline">Fiber Optic Internet</h1>
    <p class="slogan">I WENT FAST WITH<span>KORNWELL</span></p>
    <div class="speed">SPEEDS UP TO 1 GIG</div>
    <div class="price"><div class="price__label">PACKAGES<br>STARTING @</div><div class="price__amount">$55</div></div>
    <p class="txt visit">VISIT US ONLINE @</p>
    <p class="txt url">www.<b>brightwirenet</b>.example</p>
    <div class="call">CALL US AT 555-219-8063</div>
  </section>

</main>
</body>
</html>
```